Wordpress design for my private practice website - Psychotherapist

I would like a simple, clean, and elegant design for my private practice website. I work with both adults and children so I'd like it to appeal to both. However, since parents make the choice as to where to send their child for therapy, I want it to appeal to adults more. I would like the pictures on the site to have a calming effect - maybe using sand and water and rocks. I am attaching files with my company logo. I would also like my name incorporated into the header - Colette Brannigan, LCSW, Registered Play Therapist. I've also uploaded a picture of myself for my About Page.

I like the design of these 2 website and want something similar:
www.drlorapenwick.example
www.harwood-tallis.example

I would like a home page that highlights a calming graphic across the entire top of the page as well as my practice logo and my name.

I'd like a link to social media sites on the top of the homepage - facebook, pinterest.

I want a simple bar across the top with the following tabs:
Home
About Me (subtabs Who I Am, Specialties and Approach)
Counseling Services (subtabs Individual Counseling, Play Therapy, Sandplay Therapy,)
Fees
FAQs
Contact Me (would love this to be a fill in the blank contact form that sends info to my email address - should include name, phone number, email and a comment box for more information requested)
Blog (this will link with another wordpress blog)

Target Market(s)

Parents of children under age 12 with behavioral problems or are dealing with the breakup of their family through divorce - looking for someone to work with their young child. I also work with Adults that are overwhelmed and worried - often women that have many life stressors and are feeling burnt out on life and meeting everyone's needs. Families going through some type of trauma, including divorce or grief work. I also work with individuals going through a transition of religious beliefs - often exiting the religion of their youth and undergoing a crisis of faith at midlife.

Industry/Entity Type

Mental Health

Contact Information for Business Card

Colette Brannigan, LCSW
Registered Play Therapist
4917 Wexmoor Lane
Idaho Falls, Idaho 83404
(208)555-0187
www.stillbrookcounseling.example

On the opposite side, I'd like an appointment reminder area - with the following text:

Your next appointment is
_____/______/______ at ______am/pm
Please give 24 hrs notice if you need to cancel your appointment.

Coding

Coded - Design and coding required

Number of Pages Required

5+ page

Font styles to use
Sans Serif

Colors
33a6d7
9bcb3c
0355a3

Requirements
Must have
• I'd like it to be a wordpress site. I'm such a newby at web design - but I need to be able to add content and manage the site myself once it is up and running.
Nice to have
• I like the design of these 2 websites and want something similar:
• www.drlorapenwick.example
• www.harwood-tallis.example
• They are clean, easy to navigate and calming.
Should not have
• Should not look like a childcare website.

```html
<!DOCTYPE html>
<html lang="en">
<head>
<meta charset="utf-8">
<title>Stillbrook Counseling – Colette Brannigan</title>
<link href="https://fonts.googleapis.com/css2?family=Lato:wght@300;400;700&display=swap" rel="stylesheet">
<style>
:root{
  --blue:#0355a3;
  --sky:#33a6d7;
  --green:#9bcb3c;
  --ink:#1d1d1d;
  --muted:#8a8a8a;
  --line:#d6d6d6;
  --band:#f7f7f7;
  --white:#ffffff;
}
*{margin:0;padding:0;box-sizing:border-box}
html,body{width:1200px;height:2332px;overflow:hidden;background:var(--white)}
body{font-family:'Lato',sans-serif;color:var(--ink);position:relative}
section,header,nav,footer{position:relative;width:1200px}

.hero{height:572px;background:linear-gradient(180deg,#efe3d5 0%,#e7d4c3 28%,#cdb8ab 55%,#b49f98 78%,#c7b8b4 100%)}
.hero-art{position:absolute;inset:0}
.brand{position:absolute;top:92px;left:0;width:1200px;text-align:center}
.brand-mark{display:block;margin:0 auto 22px;width:44px;height:44px;border-radius:50%;background:var(--blue)}
.brand-name{font-weight:400;font-size:26px;letter-spacing:6px;color:#5d6570;text-transform:uppercase}
.name-plate{position:absolute;top:282px;left:340px;width:520px;height:72px;background:var(--blue);color:var(--white);font-weight:300;font-size:46px;letter-spacing:2px;text-align:center;line-height:72px}
.credential{position:absolute;top:364px;left:0;width:1200px;text-align:center;font-size:22px;font-weight:400;color:var(--ink)}

.main-nav{height:62px;border-bottom:1px solid var(--line)}
.main-nav a{position:absolute;top:20px;font-size:17px;color:var(--muted);text-decoration:none}
.main-nav a.active{color:var(--blue)}
.nav-dot{position:absolute;left:229px;top:58px;width:7px;height:7px;background:var(--blue)}

.intro{height:256px;text-align:center}
.section-title{font-weight:300;font-size:33px;text-transform:uppercase;letter-spacing:.5px}
.section-title.blue{color:var(--blue)}
.intro .section-title{position:absolute;top:50px;width:100%}
.intro p{position:absolute;top:118px;left:245px;width:710px;font-size:16px;line-height:27px;color:var(--muted);font-weight:400}

.services{height:439px;background:var(--band);text-align:center}
.services .section-title{position:absolute;top:66px;width:100%}
.section-lead{position:absolute;left:0;width:100%;font-size:14px;line-height:23px;color:var(--ink)}
.services .section-lead{top:126px}
.service{position:absolute;top:204px;width:233px}
.service-img{width:233px;height:124px}
.service-name{margin-top:20px;font-size:16px;text-transform:uppercase;color:var(--ink)}

.faq{height:439px}
.faq .section-title{position:absolute;top:56px;width:100%;text-align:center}
.faq-list{position:absolute;left:76px;top:160px;width:600px;list-style:none}
.faq-list li{height:63px;line-height:63px;padding-left:13px;font-size:18px;color:var(--muted);border-bottom:2px solid var(--line)}
.faq-list li:last-child{border-bottom:none}
.faq-list li.open{color:var(--sky)}
.portrait-frame{position:absolute;left:718px;top:129px;width:404px;height:290px;background:#f1f1f1;border:2px solid #dcdcdc;padding:14px}
.portrait{width:100%;height:100%;background:linear-gradient(135deg,#d8c690 0%,#c9b07a 45%,#a39563 100%)}

.blog{height:408px;background:var(--band)}
.blog .section-title{position:absolute;top:98px;width:100%;text-align:center}
.blog .section-lead{top:185px;text-align:center}
.post{position:absolute;top:260px;width:330px}
.post-title{font-size:19px;font-weight:400;color:var(--ink)}
.post-excerpt{margin-top:10px;font-size:14px;line-height:22px;color:var(--muted);width:260px}

.site-footer{height:156px;text-align:center}
.copyright{position:absolute;top:38px;width:100%;font-size:14px;color:var(--muted)}
.copyright strong{color:var(--blue);font-weight:400}
.social{position:absolute;top:82px;left:544px;display:flex;gap:18px}
.social span{display:block;width:46px;height:46px;border-radius:50%;border:1px solid #c9c9c9}
</style>
</head>
<body>

<header class="hero">
  <svg class="hero-art" role="img" aria-label="Soft-focus photograph of smooth beach pebbles at the water's edge" width="1200" height="572">
    <defs>
      <radialGradient id="glow" cx="50%" cy="20%" r="70%">
        <stop offset="0" stop-color="#fbf3ea" stop-opacity=".9"/>
        <stop offset="1" stop-color="#fbf3ea" stop-opacity="0"/>
      </radialGradient>
    </defs>
    <rect width="1200" height="572" fill="url(#glow)"/>
  </svg>
  <div class="brand">
    <span class="brand-mark"></span>
    <div class="brand-name">Stillbrook Counseling</div>
  </div>
  <h1 class="name-plate">COLETTE BRANNIGAN</h1>
  <p class="credential">LCSW, Registered Play Therapist</p>
</header>

<nav class="main-nav">
  <a class="active" href="#" style="left:216px">Home</a>
  <a href="#" style="left:345px">About Me</a>
  <a href="#" style="left:500px">Services</a>
  <a href="#" style="left:634px">Fees</a>
  <a href="#" style="left:740px">FAQ</a>
  <a href="#" style="left:818px">Blog</a>
  <a href="#" style="left:902px">Contact Us</a>
  <span class="nav-dot"></span>
</nav>

<section class="intro">
  <h2 class="section-title">Find Your Clarity</h2>
  <p>If you're looking for extra support and guidance through a challenging situation or you're just ready to move in a new direction in your life, I look forward to working with you to achieve your goals.</p>
</section>

<section class="services">
  <h2 class="section-title blue">Counseling Services</h2>
  <p class="section-lead">I work with a wide range of emotional and behavioral issues providing services that span from<br>therapy for depression and grief counseling to parenting support, couples counseling and beyond</p>
  <div class="service" style="left:202px">
    <div class="service-img" role="img" aria-label="Woman with open arms in bright sunlight" style="background:linear-gradient(135deg,#f4f0a8 0%,#9fd8b8 50%,#3fa89a 100%)"></div>
    <div class="service-name">Individual Counseling</div>
  </div>
  <div class="service" style="left:483px">
    <div class="service-img" role="img" aria-label="Parent swinging a child on the beach" style="background:linear-gradient(180deg,#bfe0e6 0%,#9fcfd6 55%,#e9ddc3 100%)"></div>
    <div class="service-name">Play Therapy</div>
  </div>
  <div class="service" style="left:764px">
    <div class="service-img" role="img" aria-label="Child playing in the sand at the shore with family behind" style="background:linear-gradient(180deg,#d9d3c8 0%,#a79886 50%,#6b5240 100%)"></div>
    <div class="service-name">Sandplay Therapy</div>
  </div>
</section>

<section class="faq">
  <h2 class="section-title">Frequently Ask Question</h2>
  <ul class="faq-list">
    <li class="open">How can therapy help me?</li>
    <li>Do I really need therapy? &nbsp;I can usually handle my problems.</li>
    <li>Why do people go to therapy and how do I know if it is right for me?</li>
    <li>Does what we talk about in therapy remain confidential?</li>
  </ul>
  <div class="portrait-frame">
    <div class="portrait" role="img" aria-label="Portrait photograph of the therapist outdoors in a golden field"></div>
  </div>
</section>

<section class="blog">
  <h2 class="section-title blue">Blog Post</h2>
  <p class="section-lead">Check out these recent Hot Topic articles! Visit this page regularly to find links to new<br>articles that will keep you informed and engaged.</p>
  <article class="post" style="left:96px">
    <h3 class="post-title">Dear High School Students</h3>
    <p class="post-excerpt">Don't let your high school years be "the best years of your life...</p>
  </article>
  <article class="post" style="left:415px">
    <h3 class="post-title">7 Ways to Cultivate More Thankfulness</h3>
    <p class="post-excerpt">Grow your gratitude with these 7 practical ideas that take 10 minutes or less...</p>
  </article>
  <article class="post" style="left:772px">
    <h3 class="post-title">Selfies Kill More People Than Sharks Do</h3>
    <p class="post-excerpt">Grow your gratitude with these 7 practical ideas that take 10 minutes or less...</p>
  </article>
</section>

<footer class="site-footer">
  <p class="copyright">© <strong>STILLBROOK COUNSELING</strong> - 2016. All Rights reserved.</p>
  <div class="social">
    <span aria-label="Social link"></span>
    <span aria-label="Social link"></span>
  </div>
</footer>

</body>
</html>
```